ZEPHIRO needs a new business card!

ZEPHIRO is a group of gaming enthusiasts who are looking for a new corporate business card.

The typeface should be modern and minimalist with attention paid to spacing between the letters and the letters 'zephiro' look relative to each other.

Should clean, crisp and minimalist - looking serious overall but with slight tweaks to the letters to make them look playful...

Black on white is fine.

Details on the card should include:
-the word 'zephiro'
-a job title (use any, for e.g. founder)
-a name (e.g. Ned Falka)
-phone number
-email address

For inspiration: http://brisket.tumblevane-cdn.example/wp-content/uploads/2013/07/mela-1.jpg

Target Market(s)

Video gaming enthusiasts

Industry/Entity Type

Business

Requirements
Must have
• Black letter on white background.
The word "zephiro"
Nice to have
• Maybe use a conservative font like Gibraltar or Helvetica and tweaking each letter individually.

You can insert normal job titles under the "zephiro" typeface
Should not have
• Should not be cartoony or childish fonts. No colors.

```html
<!DOCTYPE html>
<html lang="en">
<head>
<meta charset="utf-8">
<title>ZEPHIRO business card</title>
<link rel="stylesheet" href="https://fonts.googleapis.com/css2?family=Mulish:wght@300;400;800&display=swap">
<style>
  :root {
    --backdrop: #3b3b3b;
    --card: #ffffff;
    --ink: #000000;
    --paper-text: #ffffff;
  }
  * { margin: 0; padding: 0; box-sizing: border-box; }
  html, body {
    width: 1200px;
    height: 1001px;
    overflow: hidden;
    background: var(--backdrop);
    font-family: "Mulish", "Helvetica Neue", Arial, sans-serif;
  }
  .card {
    position: absolute;
    left: 344px;
    top: 302px;
    width: 503px;
    height: 300px;
    border-radius: 22px;
    background: var(--card);
    color: var(--ink);
    overflow: hidden;
  }
  .holder-name {
    position: absolute;
    right: 24px;
    top: 9px;
    font-size: 19px;
    font-weight: 300;
    letter-spacing: 0.2px;
  }
  .job-band {
    position: absolute;
    left: 300px;
    top: 39px;
    width: 203px;
    height: 30px;
    background: var(--ink);
    color: var(--paper-text);
    font-size: 19px;
    font-weight: 300;
    text-align: right;
    padding-right: 25px;
    line-height: 29px;
  }
  .contact {
    position: absolute;
    right: 24px;
    display: flex;
    align-items: center;
    font-size: 16px;
    font-weight: 400;
  }
  .contact svg { position: absolute; }
  .contact-phone { top: 76px; left: 300px; justify-content: flex-end; }
  .contact-phone svg { left: 2px; top: 0; }
  .contact-email { top: 103px; left: 299px; justify-content: flex-end; }
  .contact-email svg { left: 0; top: 3px; }
  .wordmark {
    position: absolute;
    left: 4px;
    top: 160px;
    font-size: 98px;
    font-weight: 800;
    line-height: 1;
    letter-spacing: 1px;
  }
</style>
</head>
<body>
  <div class="card">
    <div class="holder-name">Tomas Verel</div>
    <div class="job-band">founder</div>
    <div class="contact contact-phone">
      <svg width="12" height="19" viewBox="0 0 12 19" aria-hidden="true">
        <rect x="1" y="1" width="10" height="17" rx="2" fill="none" stroke="#000" stroke-width="1.6"/>
        <circle cx="6" cy="15" r="1.1" fill="#000"/>
      </svg>
      <span>+&nbsp; 34&nbsp; 5091 46620 3</span>
    </div>
    <div class="contact contact-email">
      <svg width="21" height="14" viewBox="0 0 21 14" aria-hidden="true">
        <rect x="0" y="0" width="21" height="14" rx="1.5" fill="#000"/>
        <path d="M1 1 L10.5 8 L20 1" fill="none" stroke="#fff" stroke-width="1.3"/>
      </svg>
      <span>zephiro@quillmail.com</span>
    </div>
    <div class="wordmark">ZEPHIRO</div>
  </div>
</body>
</html>
```